Lenny Marsh Business Cards
DJ Lenny Marsh
Simple
Lenny Marsh
DJ
4731 Corliss Street Los Angeles, CA 90041
djlennymarsh@postvale.com
djlennymarsh.com
I'd like to have a seperate email listing shown as " Bookings - kt@quillsoundagency.com"
-also under website show twitter.com/djlennymarsh
- do not show address on card
Logo on the front all other info on the back
I would like to see the color version titled "lenny-blue-grey" as well as the "lenny-white-grey"
please also try with the color "lenny-black-white". The back of the card should be very simple, nothing too crazy
Please use this logo as well. No need for headphones on the back or any fancy graphics. Please just simple text with the information I provided.Thank you.

```html
<!DOCTYPE html>
<html lang="en">
<head>
<meta charset="utf-8">
<title>Lenny Marsh Business Cards</title>
<link href="https://fonts.googleapis.com/css2?family=Comfortaa:wght@500;700&display=swap" rel="stylesheet">
<style>
  :root {
    --page: #ffffff;
    --card: #45474c;
    --text: #ffffff;
    --accent: #e3241b;
    --faint: #55575c;
  }
  * { margin: 0; padding: 0; box-sizing: border-box; }
  html, body { width: 1200px; height: 1057px; overflow: hidden; background: var(--page); }
  body { position: relative; font-family: "Comfortaa", sans-serif; color: var(--text); }
  .card {
    position: absolute;
    width: 450px;
    height: 258px;
    background: var(--card);
    border-radius: 14px;
    overflow: hidden;
  }
  .card--front { left: 144px; }
  .card--back { left: 633px; }
  .row-1 { top: 204px; }
  .row-2 { top: 627px; }

  .logo {
    position: absolute;
    left: 0; right: 0; top: 50%;
    transform: translateY(-50%);
    display: flex;
    align-items: center;
    justify-content: center;
    gap: 12px;
  }
  .logo__dot {
    width: 22px; height: 22px;
    border-radius: 50%;
    background: var(--accent);
  }
  .logo__name {
    font-weight: 700;
    font-size: 38px;
    letter-spacing: 1px;
    color: var(--text);
  }

  .back__mark {
    position: absolute;
    right: 22px; top: 78px;
    width: 160px; height: 160px;
    border-radius: 50%;
    background: var(--faint);
    opacity: 0.7;
  }
  .back__content { position: absolute; left: 33px; top: 44px; }
  .back__name { font-weight: 700; font-size: 36px; line-height: 1; }
  .back__role { font-weight: 700; font-size: 20px; color: var(--accent); margin-top: 8px; }
  .back__details { list-style: none; font-weight: 700; font-size: 14.5px; line-height: 24px; }
  .row-1 .back__details { margin-top: 36px; }
  .row-2 .back__details { margin-top: 42px; }
</style>
</head>
<body>
  <section class="card card--front row-1">
    <div class="logo"><span class="logo__name">LENNY MARSH</span><span class="logo__dot"></span></div>
  </section>
  <section class="card card--back row-1">
    <div class="back__mark" role="img" aria-label="Faint headphones decoration"></div>
    <div class="back__content">
      <h1 class="back__name">Lenny Marsh</h1>
      <p class="back__role">DJ</p>
      <ul class="back__details">
        <li>4731 Corliss Street Los Angeles, CA 90041</li>
        <li>Cell : 310-555-0148</li>
        <li>Email : djlennymarsh@postvale.com</li>
        <li>Website : www.djlennymarsh.com</li>
      </ul>
    </div>
  </section>

  <section class="card card--front row-2">
    <div class="logo"><span class="logo__name">LENNY MARSH</span><span class="logo__dot"></span></div>
  </section>
  <section class="card card--back row-2">
    <div class="back__mark" role="img" aria-label="Faint headphones decoration"></div>
    <div class="back__content">
      <h2 class="back__name">Lenny Marsh</h2>
      <p class="back__role">DJ</p>
      <ul class="back__details">
        <li>Cell : 310-555-0148</li>
        <li>Email : bookings-kt@quillsoundagency.com</li>
        <li>Website : www.djlennymarsh.com</li>
        <li>twitter.com/djlennymarsh</li>
      </ul>
    </div>
  </section>
</body>
</html>
```